Business Card design for new private practice opening

I need a business card design for my new private practice with my new logo uploaded as a file
On the front the logo
On the back: maybe a small logo somewhere?
Priv. Doz. DDr. Corinna Vestaluk
Fachärztin für Allgemein- & Viszeralchirurgie
Address: xxx
Tel: xxx
Mobil:xxx
Webseite:xxx
Email:xxx

Contact Information for Business Card

See project description above for details

Requirements
Nice to have
• I would like the colors of the logo incorporated into the business card

```html
<!DOCTYPE html>
<html lang="de">
<head>
<meta charset="utf-8">
<title>Vestaluk Chirurgie – Visitenkarte</title>
<link rel="stylesheet" href="https://fonts.googleapis.com/css2?family=Montserrat:wght@300;400;500&display=swap">
<style>
  :root {
    --backdrop: #8a8a8a;
    --card: #ffffff;
    --teal: #3fbdb7;
    --grey: #7c7c7c;
    --grey-light: #9a9a9a;
    --text: #6e6e6e;
  }
  html, body {
    margin: 0;
    width: 1200px;
    height: 1200px;
    overflow: hidden;
    background: var(--backdrop);
    font-family: "Montserrat", Arial, sans-serif;
  }
  .card {
    position: absolute;
    background: var(--card);
  }
  .card-front { left: 202px; top: 88px; width: 780px; height: 444px; }
  .card-back  { left: 197px; top: 650px; width: 777px; height: 444px; }

  .practice-name {
    position: absolute;
    left: 0; right: 0;
    margin: 0;
    text-align: center;
    color: var(--grey);
    font-weight: 400;
    letter-spacing: 0.02em;
    white-space: nowrap;
  }
  .card-front .practice-name { top: 188px; font-size: 54px; line-height: 68px; }
  .card-back .practice-name  { top: 92px;  font-size: 32px; line-height: 40px; }

  .holder-name {
    position: absolute; left: 96px; top: 213px; margin: 0;
    color: var(--teal); font-weight: 500; font-size: 31px; letter-spacing: 0.02em;
    white-space: nowrap;
  }
  .holder-title {
    position: absolute; left: 96px; top: 254px; margin: 0;
    color: var(--grey-light); font-weight: 300; font-size: 19px; letter-spacing: 0.04em;
    white-space: nowrap;
  }
  .contact-list { position: absolute; margin: 0; padding: 0; list-style: none; }
  .contact-list.left  { left: 94px; top: 299px; }
  .contact-list.right { left: 428px; top: 299px; }
  .contact-list li {
    display: flex; align-items: flex-start; gap: 8px;
    height: 35px; color: var(--text); font-size: 17.5px; line-height: 22px;
    white-space: nowrap;
  }
  .contact-list svg { flex: none; width: 22px; height: 22px; }
</style>
</head>
<body>

<section class="card card-front" aria-label="Vorderseite">
  <p class="practice-name">Vestaluk Chirurgie</p>
</section>

<section class="card card-back" aria-label="Rückseite">
  <p class="practice-name">Vestaluk Chirurgie</p>

  <h1 class="holder-name">Priv. Doz. DDr. Corinna Vestaluk</h1>
  <p class="holder-title">Fachärztin für Allgemein- &amp; Viszeralchirurgie</p>

  <ul class="contact-list left">
    <li>
      <svg viewBox="0 0 22 22" aria-hidden="true"><circle cx="11" cy="11" r="11" fill="var(--teal)"/><rect x="5.5" y="7" width="11" height="8" fill="none" stroke="#fff" stroke-width="1.4"/><path d="M5.5 7 L11 11.5 L16.5 7" fill="none" stroke="#fff" stroke-width="1.4"/></svg>
      <span>xxxxxxxxxxx@praxismail.de</span>
    </li>
    <li>
      <svg viewBox="0 0 22 22" aria-hidden="true"><circle cx="11" cy="11" r="11" fill="var(--teal)"/><path d="M7 5.5c1 0 1.6 2 1.8 2.8.2.7-.8 1.3-.8 1.6.5 1.4 2.1 3 3.5 3.5.3 0 .9-1 1.6-.8.8.2 2.8.8 2.8 1.8 0 1.4-1.4 2-2.3 2C9.5 16.4 5.6 12.5 5 8c0-1 .6-2.5 2-2.5z" fill="#fff"/></svg>
      <span>+49 000 000 0000</span>
    </li>
    <li>
      <svg viewBox="0 0 22 22" aria-hidden="true"><circle cx="11" cy="11" r="11" fill="var(--teal)"/><path d="M5 9.5c0-2 3-3 6-3s6 1 6 3v1h-3v-1.5H8v1.5H5z" fill="#fff"/><rect x="7" y="11" width="8" height="5" rx="1" fill="#fff"/><circle cx="11" cy="13.5" r="1.2" fill="var(--teal)"/></svg>
      <span>+49 000 000 0000</span>
    </li>
  </ul>

  <ul class="contact-list right">
    <li>
      <svg viewBox="0 0 22 22" aria-hidden="true"><circle cx="11" cy="11" r="11" fill="var(--teal)"/><g fill="none" stroke="#fff" stroke-width="1.2"><circle cx="11" cy="11" r="6"/><ellipse cx="11" cy="11" rx="2.6" ry="6"/><path d="M5 11h12M6 8h10M6 14h10"/></g></svg>
      <span>www.VestalukChirurgie</span>
    </li>
    <li>
      <svg viewBox="0 0 22 22" aria-hidden="true"><circle cx="11" cy="11" r="11" fill="var(--teal)"/><path d="M11 4.5a4.5 4.5 0 0 1 4.5 4.5c0 3.3-4.5 8-4.5 8s-4.5-4.7-4.5-8A4.5 4.5 0 0 1 11 4.5z" fill="#fff"/><circle cx="11" cy="9" r="1.8" fill="var(--teal)"/></svg>
      <span>000 xxxxxx, xxxx,000,<br>xxxxxx</span>
    </li>
  </ul>
</section>

</body>
</html>
```